Business start up

I need a logo within the business cards that has the name brixol with two racing stripes like the halvor racing stripes next to the name .... one of the stripes I would want to have the shades of window tint and the other stripe the colors of vinyl wrap or even the name having dripping paint of the different colors in it ... it will be a business of window tint and vinyl wrap .... service that I will be providing would be window tint Vinyl wrap Paint protection (ppfTaillights/headlights tintsBlackouts/Chrome delete Decals

Target Market(s)

Automotive

Industry/Entity Type

Automotive

Contact Information for Business Card

Have the name brixo drip like paint and have different colors dripping

Font styles to use
Serif
Sans Serif
Decorative
Script

Colors

Designer to choose colors to be used in the design.

Requirements
Nice to have
• I need a logo within the business cards that has the name brixol with two racing stripes like the halvor racing stripes next to the name .... one of the stripes I would want to have the shades of window tint and the other stripe the colors of vinyl wrap or even the name having dripping paint of the different colors in it ... it will be a business of window tint and vinyl wrap .... service that I will be providing would be
• window tint
• Vinyl wrap
• Paint protection (ppf
• Taillights/headlights tints
• Blackouts/Chrome delete
• Decals

```html
<!DOCTYPE html>
<html lang="en">
<head>
<meta charset="utf-8">
<title>Brixol Business Cards</title>
<link href="https://fonts.googleapis.com/css2?family=Mulish:wght@400;600;800&display=swap" rel="stylesheet">
<style>
  :root {
    --backdrop: #e8eaeb;
    --card-black: #171717;
    --gloss-ink: #2c2c2c;
    --silver-ink: #c9c9c9;
    --card-white: #ffffff;
    --ink: #2a2a2a;
    --accent-purple: #7a2fa3;
    --accent-blue: #2c3fa0;
    --divider: #3a3a3a;
  }
  * { box-sizing: border-box; margin: 0; padding: 0; }
  html, body { width: 1200px; height: 900px; overflow: hidden; }
  body {
    background: var(--backdrop);
    font-family: "Mulish", Arial, sans-serif;
    display: flex;
    flex-direction: column;
    align-items: center;
    justify-content: center;
    gap: 60px;
  }
  .card {
    width: 560px;
    height: 320px;
    position: relative;
    box-shadow: 0 10px 28px rgba(0,0,0,0.18), 0 2px 4px rgba(0,0,0,0.12);
  }
  /* Front */
  .card-front { background: var(--card-black); }
  .card-front .wordmark {
    position: absolute;
    left: 0; right: 0; top: 100px;
    text-align: center;
    font-weight: 800;
    font-size: 64px;
    letter-spacing: 2px;
    color: var(--gloss-ink);
  }
  .card-front .services {
    position: absolute;
    left: 0; right: 0; bottom: 40px;
    text-align: center;
    color: var(--silver-ink);
    font-size: 14px;
    line-height: 1.75;
    letter-spacing: 0.3px;
  }
  /* Back */
  .card-back { background: var(--card-white); display: flex; align-items: center; }
  .brand-block {
    width: 270px;
    display: flex;
    align-items: center;
    justify-content: center;
    gap: 10px;
  }
  .brand-block .wordmark {
    font-weight: 800;
    font-size: 44px;
    letter-spacing: 1px;
    color: var(--ink);
  }
  .brand-block .brand-square {
    width: 18px; height: 18px;
    background: var(--accent-purple);
  }
  .divider {
    width: 1px;
    height: 196px;
    background: var(--divider);
  }
  .contact-block {
    padding-left: 24px;
    color: var(--ink);
    font-size: 12.5px;
    line-height: 1.45;
  }
  .person-name {
    color: var(--accent-purple);
    font-size: 20px;
    font-weight: 600;
    text-transform: uppercase;
    line-height: 1.1;
  }
  .person-role { font-size: 14px; margin-bottom: 14px; }
  .address { margin-bottom: 14px; }
  .contact-list { list-style: none; }
  .contact-list li { display: flex; align-items: center; gap: 8px; }
  .contact-list svg { width: 11px; height: 11px; flex: none; fill: var(--accent-blue); }
</style>
</head>
<body>

<section class="card card-front" aria-label="Card front">
  <div class="wordmark">BRIXOL</div>
  <p class="services">
    Window Tint &nbsp;|&nbsp; Vinyl Wrap &nbsp;|&nbsp; Paint Protection (PPF)<br>
    Taillights/headlights tints &nbsp;|&nbsp; Blackouts/Chrome delete &nbsp;|&nbsp; Decals
  </p>
</section>

<section class="card card-back" aria-label="Card back">
  <div class="brand-block">
    <span class="wordmark">BRIXOL</span>
    <span class="brand-square"></span>
  </div>
  <div class="divider"></div>
  <div class="contact-block">
    <p class="person-name">Marcus Hale</p>
    <p class="person-role">Operational Manager</p>
    <p class="address">P/14 Ferndale Crescent Road<br>Harbor Ave, CA 40318</p>
    <ul class="contact-list">
      <li><svg viewBox="0 0 16 16"><path d="M3 1l3 3-1.5 2a9 9 0 0 0 5.5 5.5L12 10l3 3-2 2C6 14 2 10 1 3z"/></svg>+000 5550 1234</li>
      <li><svg viewBox="0 0 16 16"><path d="M4 0h8v16H4zM5.5 2v10h5V2zM7 13h2v1.5H7z" fill-rule="evenodd"/></svg>+000 5550 5678</li>
      <li><svg viewBox="0 0 16 16"><path d="M0 3h16v10H0zM1 4l7 5 7-5z" fill-rule="evenodd"/></svg>marcus.hale@brixolstudio.com</li>
      <li><svg viewBox="0 0 16 16"><path d="M8 0a8 8 0 1 0 0 16A8 8 0 0 0 8 0zm0 1.5c1 1.2 1.8 3.3 1.9 5.5H6.1C6.2 4.8 7 2.7 8 1.5zM1.6 7a6.5 6.5 0 0 1 3.3-4.7C4.4 3.7 4.1 5.3 4.1 7zm0 2h2.5c0 1.7.3 3.3.8 4.7A6.5 6.5 0 0 1 1.6 9zm4.5 0h3.8c-.1 2.2-.9 4.3-1.9 5.5-1-1.2-1.8-3.3-1.9-5.5zm5.8 0h2.5a6.5 6.5 0 0 1-3.3 4.7c.5-1.4.8-3 .8-4.7zm0-2c0-1.7-.3-3.3-.8-4.7A6.5 6.5 0 0 1 14.4 7z"/></svg>www.brixolstudio.com</li>
    </ul>
  </div>
</section>

</body>
</html>
```